Construction Company Cellar Horizon needs Business Card

I would like modern looking business card design. I am attaching logo of our company. Please include cell nr 302.481.7736 , email address cellarhorizon4u@mailvex.com, web : cellarhorizon4u.com, please also include wording: Specializing in finishing and remodeling basements. You can play with dark grey and orange colors or any ideas are welcome. Also include social media icons Chatterloop and NestFinder.

```html
<!DOCTYPE html>
<html lang="en">
<head>
<meta charset="utf-8">
<title>Cellar Horizon — Business Card</title>
<link href="https://fonts.googleapis.com/css2?family=Michroma&family=Montserrat:wght@400;500&display=swap" rel="stylesheet">
<style>
  :root {
    --page-bg: #e6e6e6;
    --card-bg: #f5f5f5;
    --card-dark: #141414;
    --accent: #f15a22;
    --ink-light: #ffffff;
    --ink-dark: #2a2a2a;
    --badge: #c9c9c9;
  }
  * { margin: 0; padding: 0; box-sizing: border-box; }
  html, body {
    width: 1200px; height: 900px; overflow: hidden;
    background: var(--page-bg);
  }
  .card {
    position: absolute; left: 130px; top: 160px;
    width: 940px; height: 580px;
    background: linear-gradient(135deg, #fafafa 0%, var(--card-bg) 60%, #ececec 100%);
    overflow: hidden;
    box-shadow: 0 10px 30px rgba(0,0,0,0.15);
  }
  .card-panel { position: absolute; inset: 0; width: 940px; height: 580px; }
  .card-panel .panel-dark { fill: var(--card-dark); }
  .card-panel .panel-edge { fill: var(--accent); }

  .tagline {
    position: absolute; left: 52px; top: 248px;
    font-family: "Michroma", sans-serif;
    font-size: 22px; line-height: 39px;
    color: var(--accent); text-transform: uppercase;
  }
  .contact {
    position: absolute; left: 52px; top: 428px;
    list-style: none;
    font-family: "Montserrat", sans-serif;
    font-size: 23px; line-height: 32px;
    color: var(--ink-light);
  }
  .contact li { display: flex; align-items: center; gap: 10px; }
  .contact svg { width: 16px; height: 16px; fill: var(--accent); flex: none; }

  .brand-name {
    position: absolute; right: 54px; top: 140px;
    font-family: "Michroma", sans-serif;
    font-size: 44px; line-height: 58px;
    color: var(--accent); text-align: right; text-transform: uppercase;
  }

  .social {
    position: absolute; right: 54px; top: 438px;
    display: flex; gap: 18px; align-items: center;
    font-family: "Montserrat", sans-serif;
    font-size: 17px; font-weight: 500; color: var(--ink-dark);
  }
  .social span { display: flex; align-items: center; gap: 6px; }
  .social i { width: 14px; height: 14px; background: var(--ink-dark); display: inline-block; }
  .listing-badge {
    position: absolute; right: 54px; top: 488px;
    width: 215px; height: 36px; border-radius: 6px;
    background: var(--badge);
  }
</style>
</head>
<body>
  <div class="card">
    <svg class="card-panel" viewBox="0 0 940 580" aria-hidden="true">
      <polygon class="panel-dark" points="0,0 80,0 672,580 0,580"/>
      <polygon class="panel-edge" points="80,0 93,0 685,580 672,580"/>
    </svg>

    <div class="brand-name">Cellar<br>Horizon</div>

    <p class="tagline">Specializing<br>in finishing<br>and remodeling<br>basements.</p>

    <ul class="contact">
      <li><svg viewBox="0 0 16 16"><path d="M4 1h8a1 1 0 0 1 1 1v12a1 1 0 0 1-1 1H4a1 1 0 0 1-1-1V2a1 1 0 0 1 1-1zm1 2v9h6V3zm3 10a.8.8 0 1 0 0 .01z"/></svg>302.481.7736</li>
      <li><svg viewBox="0 0 16 16"><path d="M8 1a7 7 0 1 0 0 14A7 7 0 0 0 8 1zm0 1.5c.7 0 1.6 1.4 1.9 4H6.1C6.4 3.9 7.3 2.5 8 2.5zM2.6 6.5h2c-.1.5-.1 1-.1 1.5s0 1 .1 1.5h-2a5.5 5.5 0 0 1 0-3zm3.5 3h3.8c-.3 2.6-1.2 4-1.9 4s-1.6-1.4-1.9-4zm5.3 0c.1-.5.1-1 .1-1.5s0-1-.1-1.5h2a5.5 5.5 0 0 1 0 3z"/></svg>cellarhorizon4u.com</li>
      <li><svg viewBox="0 0 16 16"><path d="M1 3h14v10H1zm1.5 1.5v.3L8 8.6l5.5-3.8v-.3zm0 2.1v4.9h11V6.6L8 10.4z"/></svg>cellarhorizon4u@mailvex.com</li>
    </ul>

    <div class="social">
      <span><i></i>Chatterloop</span>
      <span><i></i>NestFinder</span>
    </div>
    <div class="listing-badge" role="img" aria-label="Listing service badge"></div>
  </div>
</body>
</html>
```